Türschild, Bitte nicht stören designen für ein Hotel
Zielgruppe
Business Hotel mit Zielgruppe Business Gäste
Aufgabenstellung
Wir benötigen für unser Hotel ein Türschild, genaues mass im Anhang das wir bei Druckfuchs drucken lassen...
Seite 1:
Bitte nicht stören
Seite 2:
Ich habe ausgecheckt oder bitte reinigen Sie das Zimmer
(Da wir ein Self-Check-In Hotel sind, können die Kunden auch selber auschecken, er muss nur wenn er geht das Türschild hinhängen, sodass die Mitarbeiter wissen das Zimmer ist zu reinigen.. Aber der Kunde muss auch diese Schild aufhängen wenn er ein Sauberes Zimmer möchte wenn er ein paar Tage länger im Hotel ist... somit müssen beide Botschaften auf diese Seite sein...
Unser Hotel hat als Symbol den grauen Stuhl im Anhang, denn könnte man auf dem Türschild gross einbauen, dann würde es Symbolisch zum Hotel passen...
Von den Farben sind wir immer nur schwarz/weiss max. noch dunkel grün...
Vielen DANK
www.business-hotel-brandl.at

```html
<!DOCTYPE html>
<html lang="de">
<head>
<meta charset="utf-8">
<title>Türhänger – Stadthotel Brandl</title>
<link href="https://fonts.googleapis.com/css2?family=Montserrat:wght@600;700;800&display=swap" rel="stylesheet">
<style>
  :root {
    --backdrop: #bcd6ee;
    --paper-light: #dedede;
    --paper-dark: #1f1f1f;
    --ink-dark: #1e1e1e;
    --ink-light: #ffffff;
    --chair-light-a: #cfcfcf;
    --chair-light-b: #bdbdbd;
    --chair-dark-a: #4d4d4d;
    --chair-dark-b: #3a3a3a;
  }
  * { margin: 0; padding: 0; box-sizing: border-box; }
  html, body { width: 1200px; height: 1200px; overflow: hidden; }
  body {
    background: var(--backdrop);
    font-family: "Montserrat", sans-serif;
    position: relative;
  }
  .hanger {
    position: absolute;
    top: 60px;
    width: 430px;
    height: 1080px;
  }
  .hanger--clean { left: 125px; color: var(--ink-dark); }
  .hanger--privacy { left: 645px; color: var(--ink-light); }
  .hanger__shape { position: absolute; inset: 0; width: 430px; height: 1080px; }
  .hanger--clean .hanger__shape path { fill: var(--paper-light); }
  .hanger--privacy .hanger__shape path { fill: var(--paper-dark); }

  .brand {
    position: absolute;
    top: 368px;
    left: 0;
    width: 100%;
    display: flex;
    justify-content: center;
    align-items: center;
    gap: 9px;
    font-weight: 700;
    font-size: 22px;
    color: currentColor;
  }
  .brand__square {
    width: 14px; height: 14px;
    background: currentColor;
  }

  .chair-visual {
    position: absolute;
    z-index: 1;
    border-radius: 45% 55% 30% 30% / 40% 40% 20% 20%;
  }
  .hanger--clean .chair-visual {
    left: 45px; top: 605px; width: 340px; height: 450px;
    background: linear-gradient(160deg, var(--chair-light-a), var(--chair-light-b));
  }
  .hanger--privacy .chair-visual {
    left: 50px; top: 595px; width: 340px; height: 450px;
    background: linear-gradient(160deg, var(--chair-dark-a), var(--chair-dark-b));
  }

  .message {
    position: absolute;
    z-index: 2;
    left: 0;
    width: 100%;
    text-align: center;
    font-weight: 700;
    line-height: 1.08;
  }
  .message--away { top: 478px; font-size: 36px; }
  .message--main { top: 545px; font-size: 58px; line-height: 1.15; }
  .message--options { top: 770px; font-size: 38px; line-height: 1.15; }
  .message--options .small { font-size: 26px; display: block; margin: 2px 0; }
  .message--dnd { top: 535px; font-size: 92px; line-height: 1.15; }
</style>
</head>
<body>

  <section class="hanger hanger--clean">
    <svg class="hanger__shape" viewBox="0 0 430 1080" aria-hidden="true">
      <path fill-rule="evenodd" d="M0 215 A215 215 0 0 1 430 215 L430 1050 Q430 1080 400 1080 L30 1080 Q0 1080 0 1050 Z
        M100 200 A96 96 0 0 1 292 200 L292 290 L100 292 Z
        M292 292 L430 318 L430 346 Z"/>
    </svg>
    <div class="brand"><span class="brand__square"></span>Stadthotel Brandl</div>
    <div class="chair-visual" role="img" aria-label="Großer hellgrauer Ei-Sessel als Hotelsymbol"></div>
    <p class="message message--away">Ich bin weg…</p>
    <p class="message message--main">Sie können<br>das Zimmer<br>reinigen.</p>
    <p class="message message--options">Ausgecheckt<span class="small">oder</span>einfach nur<br>reinigen</p>
  </section>

  <section class="hanger hanger--privacy">
    <svg class="hanger__shape" viewBox="0 0 430 1080" aria-hidden="true">
      <path fill-rule="evenodd" d="M0 215 A215 215 0 0 1 430 215 L430 1050 Q430 1080 400 1080 L30 1080 Q0 1080 0 1050 Z
        M138 200 A96 96 0 0 1 330 200 L330 292 L138 290 Z
        M138 292 L0 318 L0 346 Z"/>
    </svg>
    <div class="brand"><span class="brand__square"></span>Stadthotel Brandl</div>
    <div class="chair-visual" role="img" aria-label="Großer dunkelgrauer Ei-Sessel als Hotelsymbol"></div>
    <p class="message message--dnd">Bitte<br>nicht<br>stören</p>
  </section>

</body>
</html>
```